Vorelin
Montclaro SAS
Vorelin - Personal Care
Modern
Lucila Barrios Quintero
Presidente
Av. Carrera 57 #18B-64 Bogota, Colombia
lucilabarriosquintero@correoplum.net
www.vorelin-demo.net
Vorelin is the brand;s name Montclaro SAS is the firm´s name We sell shampoo and hair tonic. çthey are good quality products, for elegant consumers.
One side can go Vorelin, the other side Montclaro, for instance. Vorelin is the important one, Vorelin has a logo I want the principal side of the business card with white background and blue letters. The other side blue background.

```html
<!DOCTYPE html>
<html lang="es">
<head>
<meta charset="utf-8">
<title>Vorelin – Stationery Set</title>
<link href="https://fonts.googleapis.com/css2?family=Raleway:wght@300;400;600&display=swap" rel="stylesheet">
<style>
  :root{
    --blue:#1f3577;
    --blue-deep:#14234f;
    --blue-light:#3d5aa8;
    --ink:#2a3a6e;
    --grey:#8a8f99;
    --silver:#d9dbe0;
    --paper:#ffffff;
    --backdrop:#5a5c60;
    --shadow:rgba(0,0,0,.18);
  }
  *{box-sizing:border-box;margin:0;padding:0}
  html,body{width:1200px;height:310px;overflow:hidden;background:#fff;
    font-family:"Raleway",Arial,sans-serif;color:var(--ink)}
  .canvas{position:relative;width:1200px;height:310px}
  .piece{position:absolute;background:var(--paper);box-shadow:0 1px 4px var(--shadow);overflow:hidden}
  .piece svg.curve{position:absolute;inset:0;width:100%;height:100%}
  .wordmark{font-family:"Raleway",Arial,sans-serif;font-weight:300;color:var(--blue);letter-spacing:.5px}

  /* logo showcase */
  .logo-showcase{position:absolute;left:12px;top:28px;width:264px;height:82px;text-align:center}
  .logo-showcase .wordmark{font-size:34px;line-height:1;display:block;margin-top:10px}
  .logo-showcase .tagline{font-size:9px;color:var(--grey);letter-spacing:1px}

  /* business cards */
  .card{width:120px;height:62px}
  .card-front{left:12px;top:120px}
  .card-info{left:144px;top:120px}
  .card-blue{left:12px;top:192px;background:var(--blue)}
  .card-silver{left:144px;top:192px;background:linear-gradient(135deg,#eef0f3,var(--silver))}
  .card .card-mark{position:absolute;left:0;right:0;top:20px;text-align:center;font-size:18px;line-height:1}
  .card-blue .card-mark{color:#fff}
  .card .small{position:absolute;left:0;right:0;bottom:5px;text-align:center;font-size:3.5px;color:var(--grey)}
  .card-blue .small{color:#c8d0e8}

  .card-info .info-mark{position:absolute;left:8px;top:20px;font-size:11px;line-height:1;text-align:left}
  .card-info .contact{position:absolute;left:56px;top:9px;width:58px;font-size:3.3px;line-height:1.45;color:var(--ink);overflow-wrap:anywhere}
  .card-info .contact strong{font-weight:600;font-size:4px;display:block}

  /* letterhead */
  .letterhead{top:19px;width:197px;height:270px}
  .letterhead.one{left:283px}
  .letterhead.two{left:492px}
  .letterhead .head-contact{position:absolute;left:48px;top:12px;font-size:3.4px;line-height:1.5;color:var(--ink)}
  .letterhead .watermark{position:absolute;left:0;right:0;top:110px;text-align:center;font-size:46px;font-weight:300;color:var(--blue);opacity:.07}
  .letterhead .footer{position:absolute;left:0;right:0;bottom:14px;text-align:center;font-size:3.4px;color:var(--grey)}

  /* envelopes */
  .envelope-small{left:703px;width:166px;height:91px}
  .envelope-small.front{top:84px}
  .envelope-small.back{top:199px;height:65px}
  .envelope-small .wordmark{position:absolute;left:12px;top:12px;font-size:12px}
  .envelope-small .footer{position:absolute;left:12px;bottom:8px;font-size:3.4px;color:var(--grey)}

  .backdrop{position:absolute;left:955px;top:0;width:245px;height:310px;background:var(--backdrop)}
  .envelope-long{left:984px;width:204px;height:72px}
  .envelope-long.blue{top:40px;background:linear-gradient(180deg,var(--blue-light),var(--blue-deep))}
  .envelope-long.grey{top:128px;background:linear-gradient(180deg,#f4f5f7,#c9ccd2)}
  .envelope-long.white{top:214px}
  .envelope-long .wordmark{position:absolute;left:0;right:0;top:38px;text-align:center;font-size:13px}
  .envelope-long.blue .wordmark{color:#fff}
</style>
</head>
<body>
<div class="canvas">

  <div class="logo-showcase">
    <span class="wordmark">Vorelin</span>
    <span class="tagline">Personal Care</span>
  </div>

  <div class="piece card card-front">
    <span class="wordmark card-mark">Vorelin</span>
    <span class="small">www.vorelin-demo.net</span>
  </div>

  <div class="piece card card-info">
    <svg class="curve" viewBox="0 0 120 62" preserveAspectRatio="none" aria-hidden="true">
      <path d="M0 62 L0 50 Q40 58 120 62 Z" fill="var(--blue)"/>
    </svg>
    <span class="wordmark info-mark">Vorelin</span>
    <div class="contact">
      <strong>Lucila Barrios Quintero</strong>
      Presidente<br>
      Av. Carrera 57 #18B-64<br>
      Bogota, Colombia<br>
      Tel. +57 1 555 0142<br>
      lucilabarriosquintero@correoplum.net
    </div>
  </div>

  <div class="piece card card-blue">
    <span class="wordmark card-mark">Vorelin</span>
    <span class="small">Montclaro SAS</span>
  </div>

  <div class="piece card card-silver">
    <span class="wordmark card-mark">Vorelin</span>
    <span class="small">www.vorelin-demo.net</span>
  </div>

  <div class="piece letterhead one">
    <svg class="curve" viewBox="0 0 197 270" preserveAspectRatio="none" aria-hidden="true">
      <path d="M150 0 Q185 10 197 55 L197 0 Z" fill="var(--blue)"/>
      <path d="M0 215 Q12 258 60 270 L0 270 Z" fill="var(--blue)"/>
    </svg>
    <div class="head-contact">Montclaro SAS<br>Av. Carrera 57 #18B-64<br>Bogota, Colombia</div>
    <div class="watermark">Vorelin</div>
    <div class="footer">www.vorelin-demo.net · lucilabarriosquintero@correoplum.net</div>
  </div>

  <div class="piece letterhead two">
    <svg class="curve" viewBox="0 0 197 270" preserveAspectRatio="none" aria-hidden="true">
      <path d="M0 0 Q10 40 0 70 Z" fill="var(--blue)"/>
      <path d="M197 215 Q185 258 137 270 L197 270 Z" fill="var(--blue)"/>
    </svg>
    <div class="watermark">Vorelin</div>
    <div class="footer">Av. Carrera 57 #18B-64 Bogota, Colombia</div>
  </div>

  <div class="piece envelope-small front">
    <svg class="curve" viewBox="0 0 166 91" preserveAspectRatio="none" aria-hidden="true">
      <path d="M0 0 Q8 45 0 91 Z" fill="var(--blue)"/>
    </svg>
    <span class="wordmark">Vorelin</span>
    <span class="footer">Av. Carrera 57 #18B-64 Bogota, Colombia</span>
  </div>

  <div class="piece envelope-small back">
    <svg class="curve" viewBox="0 0 166 65" preserveAspectRatio="none" aria-hidden="true">
      <path d="M120 65 Q155 55 166 30 L166 65 Z" fill="var(--blue)"/>
    </svg>
    <span class="footer">www.vorelin-demo.net</span>
  </div>

  <div class="backdrop"></div>

  <div class="piece envelope-long blue">
    <svg class="curve" viewBox="0 0 204 72" preserveAspectRatio="none" aria-hidden="true">
      <path d="M0 0 L102 34 L204 0" fill="none" stroke="rgba(255,255,255,.25)" stroke-width="1"/>
    </svg>
    <span class="wordmark">Vorelin</span>
  </div>

  <div class="piece envelope-long grey">
    <svg class="curve" viewBox="0 0 204 72" preserveAspectRatio="none" aria-hidden="true">
      <path d="M0 0 L102 30 L204 0" fill="none" stroke="rgba(0,0,0,.12)" stroke-width="1"/>
    </svg>
  </div>

  <div class="piece envelope-long white">
    <svg class="curve" viewBox="0 0 204 72" preserveAspectRatio="none" aria-hidden="true">
      <path d="M0 0 L102 36 L204 0" fill="none" stroke="rgba(0,0,0,.15)" stroke-width="1"/>
      <path d="M0 72 L80 30 M204 72 L124 30" fill="none" stroke="rgba(0,0,0,.08)" stroke-width="1"/>
    </svg>
  </div>

</div>
</body>
</html>
```